Professional Letterhead for electronic use

I would like to inquire, if you could help me to create a letterhead, mostly for electronic use. Preferably in word file, with fixed letterhead design (header and footer), but will allow to add text on the main body of the letter. I usually operate online and would like to be able to add text, convert it to PDF and send as an attachment.
Target Market(s)
High net worth clients.
Industry/Entity Type
Real Estate Agent
Font styles to use
Other font styles liked:
- Century Gothic
Requirements
Must have
- Company name, logo, full address, email address, landline number, website address, Homestead Adjudicator logo, PELV logo, Company registration number
Nice to have
- Professional and elegant design

```html
<!DOCTYPE html>
<html lang="en">
<head>
<meta charset="utf-8">
<title>Corvane Estate Agents – Letterhead and Folder</title>
<link rel="stylesheet" href="https://fonts.googleapis.com/css2?family=Didact+Gothic&family=Questrial&display=swap">
<style>
  :root {
    --backdrop: #e4e7e8;
    --paper: #ffffff;
    --plum: #4a1a31;
    --plum-deep: #431629;
    --plum-light: #561d38;
    --orange: #e8541f;
    --orange-soft: #f39366;
    --blush: #fbe6dc;
    --ink: #3c3c3c;
    --navy: #1d3f7a;
    --green: #2f7d32;
  }
  * { box-sizing: border-box; margin: 0; padding: 0; }
  html, body { width: 1200px; height: 784px; overflow: hidden; }
  body {
    background: radial-gradient(ellipse at center, #f2f4f4 0%, var(--backdrop) 100%);
    font-family: "Didact Gothic", "Century Gothic", sans-serif;
    position: relative;
  }
  .sheet {
    position: absolute; top: 45px; width: 513px; height: 697px;
    border-radius: 14px; overflow: hidden;
    box-shadow: 0 2px 6px rgba(0,0,0,.18);
  }
  .letterhead { left: 42px; background: var(--paper); }
  .folder {
    left: 634px;
    background: linear-gradient(180deg, var(--plum-light) 0%, var(--plum-deep) 100%);
  }

  /* letterhead header */
  .brand { position: absolute; top: 16px; left: 150px; display: flex; align-items: center; gap: 12px; }
  .brand-mark { width: 52px; height: 52px; border-radius: 50%;
    background: linear-gradient(135deg, var(--orange-soft), var(--orange)); }
  .brand-name { font-family: "Questrial", sans-serif; font-size: 27px; letter-spacing: 5px; color: var(--plum); line-height: 1; }
  .brand-tag { font-size: 10.5px; letter-spacing: 2.6px; color: var(--orange); margin-top: 7px; }
  .rule { position: absolute; top: 96px; left: 33px; width: 446px; height: 2px; background: var(--plum); }
  .contacts { position: absolute; top: 102px; left: 0; width: 100%; display: flex; justify-content: center; gap: 12px;
    font-size: 9.5px; color: var(--ink); }
  .contacts span { display: inline-flex; align-items: center; gap: 4px; }
  .contacts svg { width: 9px; height: 9px; fill: var(--orange); }

  /* letter body */
  .letter-body { position: absolute; top: 153px; left: 43px; width: 428px; font-size: 11px; line-height: 17.7px; color: var(--ink); text-align: justify; hyphens: auto; }
  .letter-body p + p { margin-top: 17.7px; }

  .watermark { position: absolute; left: 255px; top: 425px; width: 320px; height: 320px; border-radius: 50%;
    background: var(--blush); opacity: .7; }

  .signature { position: absolute; top: 597px; left: 380px; color: var(--ink); }
  .signature-name { font-size: 14px; }
  .signature-role { font-size: 10px; margin-top: 6px; }

  .memberships { position: absolute; top: 640px; left: 42px; display: flex; align-items: center; gap: 10px; }
  .badge-adjudicator { width: 61px; height: 22px; background: var(--navy); }
  .badge-pelv { width: 30px; height: 30px; border-radius: 50%; background: var(--green); }

  .website { position: absolute; bottom: 10px; left: 0; width: 100%; text-align: center; font-size: 10.5px; letter-spacing: 2.4px; color: var(--ink); }

  /* folder */
  .folder-tab { position: absolute; right: 0; top: 150px; width: 34px; height: 260px;
    background: var(--plum-deep); border-radius: 30px 0 0 0; opacity: .6; }
  .folder-mark { position: absolute; left: 200px; top: 391px; width: 130px; height: 130px; border-radius: 50%;
    background: linear-gradient(135deg, var(--orange-soft), var(--orange)); }
  .folder-name { position: absolute; top: 546px; left: 0; width: 100%; text-align: center;
    font-family: "Questrial", sans-serif; font-size: 38px; letter-spacing: 8px; color: #fff; }
  .folder-tag { position: absolute; top: 602px; left: 0; width: 100%; text-align: center;
    font-size: 15.5px; letter-spacing: 5px; color: var(--orange); }
</style>
</head>
<body>
  <section class="sheet letterhead">
    <div class="watermark" aria-hidden="true"></div>
    <header>
      <div class="brand">
        <div class="brand-mark" aria-hidden="true"></div>
        <div>
          <div class="brand-name">CORVANE</div>
          <div class="brand-tag">ESTATE AGENTS</div>
        </div>
      </div>
      <div class="rule"></div>
      <div class="contacts">
        <span><svg viewBox="0 0 10 10"><path d="M1 3c0-1 1-2 4-2s4 1 4 2v1H7V3H3v1H1zM2 5h6l1 4H1z"/></svg>(555) 301-4420</span>
        <span><svg viewBox="0 0 10 10"><path d="M3 1h4v2H3zM1 4h8v4H7v1H3V8H1zM3 6v2h4V6z"/></svg>(555) 301-4488</span>
        <span><svg viewBox="0 0 10 10"><path d="M5 0a3.5 3.5 0 0 0-3.5 3.5C1.5 6 5 10 5 10s3.5-4 3.5-6.5A3.5 3.5 0 0 0 5 0zm0 5a1.5 1.5 0 1 1 0-3 1.5 1.5 0 0 1 0 3z"/></svg>1480 Harrow Lane, Brookfield, MI 48210</span>
      </div>
    </header>

    <main class="letter-body">
      <p>Lorem ipsum dolor sit amet, consectetur adipiscing elit. Donec orci purus, luctus vitae dignissim eu, iaculis sed purus. Vivamus faucibus, ipsum nec aliquet viverra, leo mauris condimentum ligula, sit amet sagittis enim ligula quis arcu. Nam egestas tortor id nisi porttitor mattis. In tortor ante, ultricies in suscipit a, tempus non massa. Vivamus et auctor mi. Fusce vel massa nulla. Phasellus nec eros mauris, et scelerisque orci. Donec malesuada orci vitae nulla accumsan porta a id massa.</p>
      <p>Quisque accumsan iaculis magna sit amet fringilla. Maecenas consequat, magna eget tincidunt semper, odio nibh rutrum mi, id feugiat ante nisi eu risus. Vestibulum nunc orci, rhoncus a placerat in, ultricies in mi. Cras mattis varius eros, vel fringilla nisi suscipit eget. Quisque scelerisque sagittis nulla at porttitor. Mauris a justo et tellus interdum tristique. Sed id augue vitae urna euismod commodo aliquet a quam. Pellentesque arcu velit, cursus et malesuada ut, consequat et diam. Nullam erat sem, rhoncus id ullamcorper vitae, rhoncus et arcu. In ultricies ultricies nulla.</p>
      <p>Kut rutrum nisi iaculis at. Donec eu magna a metus ornare faucibus. Fusce aliquet faucibus ultricies. Morbi semper, est id tincidunt gravida, sem arcu adipiscing lacus, ac bibendum nulla leo eu purus. Quisque nec diam sed risus consectetur a ccumsan quis quis nibh. Vestibulum id purus lorem. Donec eu magna a metus ornare faucibus. Fusce aliquet faucibus ultricies. Morbi semper, est id tincidunt gravida, sem arcu adipiscing lacus, ac bibendum nulla leo eu purus. Quisque nec diam sed risus consectetur a ccumsan quis quis nibh. Vestibulum id purus lorem.</p>
    </main>

    <div class="signature">
      <div class="signature-name">Elias Varn</div>
      <div class="signature-role">Co-Founder &amp; CEO</div>
    </div>

    <footer>
      <div class="memberships">
        <div class="badge-adjudicator" role="img" aria-label="Homestead Adjudicator membership badge"></div>
        <div class="badge-pelv" role="img" aria-label="PELV membership badge"></div>
      </div>
      <div class="website">www.corvaneestate.org</div>
    </footer>
  </section>

  <section class="sheet folder">
    <div class="folder-tab" aria-hidden="true"></div>
    <div class="folder-mark" aria-hidden="true"></div>
    <div class="folder-name">CORVANE</div>
    <div class="folder-tag">ESTATE AGENTS</div>
  </section>
</body>
</html>
```